Norwegian psychologist service needs a fresh and exiting web site*

Norwegian psychologist service: working with therapy, personal development, mastery and personal growth. Focus: children and teenagers with special needs; family dynamics; group processes; individuals with a need for therapy and personal growth. (Our company name: Kildeløft og ro (means Mastery and Growth).

We already have a logo for the company, which will be used (will be attached in the project).

The webside is to be structured in 4 pages with roll down curtain menus (the numbers are just for guiding the designer - the should not be added):

Page 1: Om Kildeløft og Ro (about Mastery and Growth): this is where our business is is presented/described shortly: Lorem Ipsum dolor cit...

Page 2: Tjenester (Services): this is where our 5 service areas are presented:
2.1 Utredning (Investigation, diagnosing): Lorem Ipsum dolor cit...
2.2 Rådgivning (consulting): Lorem Ipsum dolor cit...

2.3 Kurs og work shops (courses and work shops): Lorem Ipsum dolor cit...
2.3a Kildeløft og ro Tema 1 (T1)
2.3b Kildeløft og ro Tema 2 (T2)
2.3c Kildeløft og ro Tema 3 (T3)

2.4 Terapi og utvikling (Therapy and development)
2.4a Kildeløft og ro for individer (KR1)
2.4b Kildeløft og ro i familier (KR2)
2.4c Kildeløft og ro i grupper (KR3)
2.4d Kildeløft og ro i institusjoner (KR4)

Page 3: Aktuelt (Blog): this is our blog where we share knowledge and articles

Page 4: Kontakt (Contact): This is the contact form page. Contact form should constitute:
- Ditt navn (your name)
- E-post (your e-mail)
- Emne (subject)
- Melding (message/description)

Our project should also include suggestion for handheld units (iPhone, iPad).
Updates

We have both been traveling with work for a while, and then unfortunately both of us got sick on return, so we need a few more days to evaluate and choose design. Kind Regards Arne & Ragnhild

Target Market(s)

Focus on therapy, learning, mastery and growth for children and teenagers with special needs, within the family dynamics, or in a group setting.
OUR MARKETS:
Private market: individuals, families, groups and health industry institutions (with focus on learning, mastery, growth (as well as growing up) and psychiatry for children and teenagers with special difficulties and needs)
Public institutions: Government institutions, state institutions and municipality institutions (e.g. schools, municipality health service, hospitals) that serve the public (families with children and teenagers with special needs, and where learning, mastery, growth (as well as growing up) and potential psychiatry is an issue).

Number of Pages Required

4 page

Font styles to use
Sans Serif

Colors

Designer to choose colors to be used in the design.

Requirements
Must have
• The website must have 4 pages with roll down curtain menus (we have added a PDF with suggested structure, and headings, with sub menus - see attached PDF drawing.
• The web page must also use the added logo file - and make the web page work well with our logo.
• We would like the website to have a modern look and we would like the site to be associated with typical HIGH END TOP QUALITY private health institutions, but with a stronger focus on human beings (hands, faces etc), and not white coats and doctors. We are psychologists in the private market.
• For instance, if photos are being used - we tend to like "warm" almost art-like, "grainy" two-tone (e.g. sepia) photos to illustrate our focus. If designer can find such photos as part of design, it would be interesting to us. We would like a few photos like that integrated in the design.
• We also want a design suggestion for how the web page should look like and behave on handheld units (e.g. iPhone, iPad).
Nice to have
• If designer could find a number of suitable photos that matches the business idea and design requirements (see description above), that could follow website, that would be good.
• It could also be nice to have graphic symbols that denote the different pages/subpages (subjects)....
• HORSES: we sometimes use horses as a "tool" in therapy sessions. The horse is not necessarily used for riding, but for contact, communication and grooming. PHOTOS: we would like the designer to find an opportunity for using a photo reflecting this cooperation between therapist, child, teenager and horse. It is a bit up to the designer to find a way to do this... Since the horse is only a tool, among many other tools, it does not have to be much - but we want to try and see how it will work with a photo that also reflects this part of our business.

```html
<!DOCTYPE html>
<html lang="no">
<head>
<meta charset="utf-8">
<title>Aktuelt – Kildeløft og Ro</title>
<link rel="stylesheet" href="https://fonts.googleapis.com/css2?family=Playfair+Display:wght@400;700&display=swap">
<style>
  :root {
    --ink: #2b3d8c;
    --ink-dark: #27345e;
    --body: #3c3c44;
    --accent: #36c27a;
    --panel: #c2d9d8;
    --rule: #d6d6da;
    --panel-rule: #9fbcbc;
    --muted: #9a9aa2;
    --paper: #ffffff;
  }
  * { box-sizing: border-box; margin: 0; padding: 0; }
  html, body { width: 1200px; height: 3612px; overflow: hidden; background: var(--paper); }
  body { position: relative; font-family: "Playfair Display", Georgia, serif; color: var(--body); }

  .site-header { position: absolute; left: 0; top: 0; width: 1200px; height: 165px; border-bottom: 1px solid var(--rule); }
  .nav-link { position: absolute; top: 68px; font-size: 14px; font-weight: 700; color: var(--ink); text-decoration: none; }
  .nav-about { left: 125px; }
  .nav-services { left: 334px; }
  .nav-services svg { position: absolute; left: 80px; top: 5px; }
  .nav-blog { left: 791px; }
  .nav-contact { left: 910px; }
  .brand { position: absolute; left: 450px; width: 300px; top: 56px; text-align: center; }
  .brand-mark { display: block; width: 34px; height: 34px; margin: 0 auto 8px; border-radius: 50%; background: var(--ink); }
  .brand-name { font-size: 22px; font-weight: 400; color: var(--ink); letter-spacing: 0.5px; }
  .search { position: absolute; left: 1031px; top: 55px; width: 46px; height: 46px; border: 1px solid var(--rule); border-radius: 50%; }
  .search svg { position: absolute; left: 13px; top: 13px; }

  .post { position: absolute; left: 125px; width: 562px; }
  .post-title { font-size: 28px; line-height: 36px; font-weight: 700; color: var(--ink); text-transform: uppercase; letter-spacing: 0.2px; }
  .post-media { height: 331px; margin-top: 19px; }
  .post-excerpt { margin-top: 24px; font-size: 12.6px; line-height: 23.5px; color: var(--body); }
  .read-more { display: inline-block; margin-top: 30px; font-size: 12.5px; font-weight: 700; color: var(--accent); text-transform: uppercase; text-decoration: none; }
  .read-more svg { margin-left: 10px; vertical-align: -1px; }

  .media-road { background: linear-gradient(180deg, #7a98c4 0%, #b5c3d6 40%, #a58c72 62%, #5a5556 100%); }
  .media-lake { background: linear-gradient(180deg, #dfe4ea 0%, #c7ccd3 30%, #8d8786 48%, #a9b4c0 62%, #5d5148 100%); }
  .media-shore { background: linear-gradient(180deg, #e6e1dc 0%, #a9a2a3 35%, #8f9fb3 62%, #c8b0a8 100%); }
  .media-hands { background: radial-gradient(ellipse at 45% 60%, #b58b7a 0%, #7c4d66 35%, #a8a2c8 70%, #6d6aa6 100%); }
  .media-field { background: linear-gradient(180deg, #f1ece2 0%, #4b4530 28%, #8d6a28 55%, #c89a3a 80%, #9a7125 100%); }

  .sidebar { position: absolute; left: 813px; top: 262px; width: 262px; }
  .sidebar-heading { font-size: 16px; line-height: 26px; font-weight: 700; color: var(--ink-dark); text-transform: uppercase; }
  .recent-list { margin-top: 18px; background: var(--panel); padding: 0 21px; height: 1278px; }
  .recent-item { height: 255.6px; padding-top: 20px; border-bottom: 1px solid var(--panel-rule); }
  .recent-item:last-child { border-bottom: 0; }
  .recent-title { font-size: 15.5px; line-height: 23px; font-weight: 700; color: var(--ink-dark); text-transform: uppercase; }
  .recent-date { margin-top: 5px; font-size: 13px; line-height: 20px; color: var(--ink-dark); text-transform: uppercase; }
  .recent-excerpt { margin-top: 13px; font-size: 12px; line-height: 20px; color: #4e5a6a; }
  .recent-item .read-more { margin-top: 6px; font-size: 11px; }
  .recent-item .read-more svg { margin-left: 6px; }

  .site-footer { position: absolute; left: 0; top: 3584px; width: 1200px; text-align: center; font-size: 10px; color: var(--muted); }
</style>
</head>
<body>
  <header class="site-header">
    <a class="nav-link nav-about" href="#">Om Kildeløft og Ro</a>
    <a class="nav-link nav-services" href="#">Tjenester
      <svg width="12" height="8" viewBox="0 0 12 8"><path d="M1 1l5 5 5-5" fill="none" stroke="#2b3d8c" stroke-width="1.2"/></svg>
    </a>
    <div class="brand">
      <span class="brand-mark"></span>
      <span class="brand-name">Kildeløft og Ro</span>
    </div>
    <a class="nav-link nav-blog" href="#">Aktuelt</a>
    <a class="nav-link nav-contact" href="#">Kontakt</a>
    <div class="search">
      <svg width="20" height="20" viewBox="0 0 20 20"><circle cx="8.5" cy="8.5" r="6.5" fill="none" stroke="#2b3d8c" stroke-width="1.4"/><path d="M13.3 13.3L18 18" stroke="#2b3d8c" stroke-width="1.4"/></svg>
    </div>
  </header>

  <article class="post" style="top:262px">
    <h2 class="post-title">Nam ac ullamcorper dolor</h2>
    <div class="post-media media-road" role="img" aria-label="Photo: two women walking hand in hand along a desert road toward mountains"></div>
    <p class="post-excerpt">Lorem ipsum dolor sit amet, consectetur adipiscing elit. Curabitur vehicula, enim eget viverra interdum, dui quam fermentum nibh, vitae commodo ligula nulla in sem. Curabitur at libero eu magna laoreet rutrum. Nam commodo venenatis quam, eu volutpat risus posuere nec. Donec a condimentum quam, eu condimentum libero.</p>
    <a class="read-more" href="#">Les videre<svg width="6" height="10" viewBox="0 0 6 10"><path d="M1 1l4 4-4 4" fill="none" stroke="#36c27a" stroke-width="1.2"/></svg></a>
  </article>

  <article class="post" style="top:910px">
    <h2 class="post-title">Nam ac ullamcorper dolor</h2>
    <div class="post-media media-lake" role="img" aria-label="Photo: a man standing on a rock by a calm lake with hills behind"></div>
    <p class="post-excerpt">Lorem ipsum dolor sit amet, consectetur adipiscing elit. Curabitur vehicula, enim eget viverra interdum, dui quam fermentum nibh, vitae commodo ligula nulla in sem. Curabitur at libero eu magna laoreet rutrum. Nam commodo venenatis quam, eu volutpat risus posuere nec. Donec a condimentum quam, eu condimentum libero.</p>
    <a class="read-more" href="#">Les videre<svg width="6" height="10" viewBox="0 0 6 10"><path d="M1 1l4 4-4 4" fill="none" stroke="#36c27a" stroke-width="1.2"/></svg></a>
  </article>

  <article class="post" style="top:1558px">
    <h2 class="post-title">Nam ac ullamcorper dolor</h2>
    <div class="post-media media-shore" role="img" aria-label="Photo: two small children holding hands at the water's edge"></div>
    <p class="post-excerpt">Lorem ipsum dolor sit amet, consectetur adipiscing elit. Curabitur vehicula, enim eget viverra interdum, dui quam fermentum nibh, vitae commodo ligula nulla in sem. Curabitur at libero eu magna laoreet rutrum. Nam commodo venenatis quam, eu volutpat risus posuere nec. Donec a condimentum quam, eu condimentum libero.</p>
    <a class="read-more" href="#">Les videre<svg width="6" height="10" viewBox="0 0 6 10"><path d="M1 1l4 4-4 4" fill="none" stroke="#36c27a" stroke-width="1.2"/></svg></a>
  </article>

  <article class="post" style="top:2206px">
    <h2 class="post-title">Nam ac ullamcorper dolor</h2>
    <div class="post-media media-hands" role="img" aria-label="Photo: cupped hands holding dried rose petals"></div>
    <p class="post-excerpt">Lorem ipsum dolor sit amet, consectetur adipiscing elit. Curabitur vehicula, enim eget viverra interdum, dui quam fermentum nibh, vitae commodo ligula nulla in sem. Curabitur at libero eu magna laoreet rutrum. Nam commodo venenatis quam, eu volutpat risus posuere nec. Donec a condimentum quam, eu condimentum libero.</p>
    <a class="read-more" href="#">Les videre<svg width="6" height="10" viewBox="0 0 6 10"><path d="M1 1l4 4-4 4" fill="none" stroke="#36c27a" stroke-width="1.2"/></svg></a>
  </article>

  <article class="post" style="top:2854px">
    <h2 class="post-title">Nam ac ullamcorper dolor</h2>
    <div class="post-media media-field" role="img" aria-label="Photo: a girl walking through a golden wheat field at sunset"></div>
    <p class="post-excerpt">Lorem ipsum dolor sit amet, consectetur adipiscing elit. Curabitur vehicula, enim eget viverra interdum, dui quam fermentum nibh, vitae commodo ligula nulla in sem. Curabitur at libero eu magna laoreet rutrum. Nam commodo venenatis quam, eu volutpat risus posuere nec. Donec a condimentum quam, eu condimentum libero.</p>
    <a class="read-more" href="#">Les videre<svg width="6" height="10" viewBox="0 0 6 10"><path d="M1 1l4 4-4 4" fill="none" stroke="#36c27a" stroke-width="1.2"/></svg></a>
  </article>

  <aside class="sidebar">
    <h3 class="sidebar-heading">Siste innlegg</h3>
    <div class="recent-list">
      <div class="recent-item">
        <h4 class="recent-title">Donec non dolor eget felis consequat porttitor quis sed dui</h4>
        <p class="recent-date">22. February 2020</p>
        <p class="recent-excerpt">Proin consequat risus a nisl tempor fringilla in vitae tortor. Suspendisse tincidunt lectus accumsan commodo lacinia.</p>
        <a class="read-more" href="#">Les videre<svg width="5" height="8" viewBox="0 0 6 10"><path d="M1 1l4 4-4 4" fill="none" stroke="#36c27a" stroke-width="1.2"/></svg></a>
      </div>
      <div class="recent-item">
        <h4 class="recent-title">Donec non dolor eget felis consequat porttitor quis sed dui</h4>
        <p class="recent-date">22. February 2020</p>
        <p class="recent-excerpt">Proin consequat risus a nisl tempor fringilla in vitae tortor. Suspendisse tincidunt lectus accumsan commodo lacinia.</p>
        <a class="read-more" href="#">Les videre<svg width="5" height="8" viewBox="0 0 6 10"><path d="M1 1l4 4-4 4" fill="none" stroke="#36c27a" stroke-width="1.2"/></svg></a>
      </div>
      <div class="recent-item">
        <h4 class="recent-title">Donec non dolor eget felis consequat porttitor quis sed dui</h4>
        <p class="recent-date">22. February 2020</p>
        <p class="recent-excerpt">Proin consequat risus a nisl tempor fringilla in vitae tortor. Suspendisse tincidunt lectus accumsan commodo lacinia.</p>
        <a class="read-more" href="#">Les videre<svg width="5" height="8" viewBox="0 0 6 10"><path d="M1 1l4 4-4 4" fill="none" stroke="#36c27a" stroke-width="1.2"/></svg></a>
      </div>
      <div class="recent-item">
        <h4 class="recent-title">Donec non dolor eget felis consequat porttitor quis sed dui</h4>
        <p class="recent-date">22. February 2020</p>
        <p class="recent-excerpt">Proin consequat risus a nisl tempor fringilla in vitae tortor. Suspendisse tincidunt lectus accumsan commodo lacinia.</p>
        <a class="read-more" href="#">Les videre<svg width="5" height="8" viewBox="0 0 6 10"><path d="M1 1l4 4-4 4" fill="none" stroke="#36c27a" stroke-width="1.2"/></svg></a>
      </div>
      <div class="recent-item">
        <h4 class="recent-title">Donec non dolor eget felis consequat porttitor quis sed dui</h4>
        <p class="recent-date">22. February 2020</p>
        <p class="recent-excerpt">Proin consequat risus a nisl tempor fringilla in vitae tortor. Suspendisse tincidunt lectus accumsan commodo lacinia.</p>
        <a class="read-more" href="#">Les videre<svg width="5" height="8" viewBox="0 0 6 10"><path d="M1 1l4 4-4 4" fill="none" stroke="#36c27a" stroke-width="1.2"/></svg></a>
      </div>
    </div>
  </aside>

  <footer class="site-footer">©2020 Kildeløft og Ro. All Rights Reserved.</footer>
</body>
</html>
```